R&T Cleanwave Stripping Business Card

We are in need of a business card design for our new Texas based company called 'R&T Cleanwave Stripping'. Our new innovative mobile media blasting service utilizes recycled material and a new water based process that eliminates all dust (i.e. as apposed to the old sand blasting format). Our 'advanced surface preparation' service targets multiple industries such as automotive, Industrial, marine and structural (graffiti removal). We would like to see the design include a recycling type logo or concept that utilizes colors such as black, various shades of green, some white, yellow and/or grey (e.g. perhaps a blackish background). The final design should look simple and professional and should clearly communicate the environmentally friendly approach through logo or design (i.e. Eco-Friendly, Go Green or Blast Green methodologies). Thank you in advance!
Updates

Please pardon any inconvenience. We have decided to pursue a two sided business card. All original information/designs requirements remains the same for the front. However, we would like back of the card to state the following: "We bring the power of Hydroveil Media Scouring equipment to your location. We can remove any coating from any surface. Bullets include: Paint Stripping, Auto Restoration, Graffiti Removal, Black Walls & Stone, Concrete, Boats, Iron Fences, Tractors & Trailers, Pools & Fountains, Wood Restoration.

Industry/Entity Type

Recycling

Contact Information for Business Card

R&T Cleanwave Stripping, LLC - Gordon Pelly, MBA, PMP - cell: 915-382-6091, office: 915-627-8853 - gpelly@rtcleanwavestripping.com - CEO/Founder

Requirements
Must have
• Recycle or environmentally friendly logos or design.
Nice to have
• Business oriented design with an aggressive look. Also, if possible would like to see R&T incorporated into the design or logo. Please note that we have decided to add the option of adding details to the back of the card (2 sided). The front should contain the logo/design and the back should have the following details listed: "We bring the power of Hydroveil Media Scouring equipment to your location. We can remove any coating from any surface. Bullets include: Paint Stripping, Auto Restoration, Graffiti Removal, Black Walls & Stone, Concrete, Boats, Iron Fences, Tractors & Trailers, Pools & Fountains, Wood Restoration.

```html
<!DOCTYPE html>
<html lang="en">
<head>
<meta charset="utf-8">
<title>R&amp;T Cleanwave Stripping – Card Back</title>
<link rel="stylesheet" href="https://fonts.googleapis.com/css2?family=Arimo:wght@700&family=Oswald:wght@600&family=Rubik+Dirt&display=swap">
<style>
  :root {
    --bg-dark: #141414;
    --bg-mid: #2a2a2a;
    --green: #17a317;
    --green-bright: #1fb51f;
    --white: #ffffff;
    --shadow: rgba(0,0,0,0.9);
  }
  html, body {
    margin: 0;
    padding: 0;
    width: 1200px;
    height: 900px;
    overflow: hidden;
    background: var(--bg-dark);
  }
  .card-back {
    position: relative;
    width: 1200px;
    height: 900px;
    background:
      radial-gradient(ellipse at 50% 40%, var(--bg-mid) 0%, #1c1c1c 55%, var(--bg-dark) 100%);
    overflow: hidden;
  }
  .brand-mark {
    position: absolute;
    left: 0;
    width: 1200px;
    top: 110px;
    text-align: center;
    font-family: "Arimo", Arial, sans-serif;
    font-weight: 700;
    font-size: 110px;
    line-height: 1;
    color: var(--green-bright);
    letter-spacing: 2px;
  }
  .tagline {
    position: absolute;
    left: 0;
    width: 1200px;
    text-align: center;
    font-family: "Arimo", Arial, sans-serif;
    font-weight: 700;
    text-shadow: 2px 2px 4px var(--shadow);
    white-space: nowrap;
  }
  .tagline--power {
    top: 336px;
    font-size: 22px;
    color: var(--green);
  }
  .tagline--coating {
    top: 393px;
    font-size: 27px;
    color: var(--white);
  }
  .grunge {
    font-family: "Rubik Dirt", Impact, sans-serif;
    font-weight: 400;
    letter-spacing: 1px;
  }
  .grunge--service {
    font-size: 30px;
    color: var(--white);
    text-transform: uppercase;
  }
  .grunge--any {
    font-size: 36px;
    color: var(--green);
  }
  .service-list {
    position: absolute;
    margin: 0;
    padding: 0;
    list-style: none;
    text-align: center;
    font-family: "Oswald", "Arial Narrow", sans-serif;
    font-weight: 600;
    text-shadow: 3px 3px 5px var(--shadow);
    letter-spacing: -0.5px;
  }
  .service-list--left {
    left: 210px;
    width: 400px;
    top: 494px;
    font-size: 32px;
    line-height: 44.6px;
  }
  .service-list--right {
    left: 626px;
    width: 400px;
    top: 496px;
    font-size: 34px;
    line-height: 49.8px;
  }
  .service-list li:nth-child(odd) { color: var(--green); }
  .service-list li:nth-child(even) { color: var(--white); }
</style>
</head>
<body>
  <main class="card-back">
    <div class="brand-mark">R&amp;T</div>

    <p class="tagline tagline--power" style="margin:0">
      We bring the power of <span class="grunge grunge--service">Hydroveil Media Scouring</span> equipment to your location.
    </p>
    <p class="tagline tagline--coating" style="margin:0">
      We can remove <span class="grunge grunge--any">ANY</span> coating from <span class="grunge grunge--any">ANY</span> surface.
    </p>

    <ul class="service-list service-list--left">
      <li>Paint Stripping</li>
      <li>Auto Restoration</li>
      <li>Graffiti Removal</li>
      <li>Black Walls &amp; Stone</li>
      <li>Concrete</li>
      <li>Boats</li>
    </ul>

    <ul class="service-list service-list--right">
      <li>Iron Fences</li>
      <li>Tractors</li>
      <li>Trailers</li>
      <li>Pools &amp; Fountains</li>
      <li>Wood Restoration</li>
    </ul>
  </main>
</body>
</html>
```